Flight school needs business cards!

We need a cool business card design for two flight school employees. The Chief Flight Instructor and the Manager. Put simply, we teach people how to fly. I would think it would be cool to have the front of the business card look like a pilot's license (US pilot certificate) and the backside has the logo and contact information.

Target Market(s)

Someone who wants to learn how to fly.

Industry/Entity Type

Aviation

Requirements
Must have
• The front of the business card should look like a United States pilot license, and it should read:

Your Name Here
Your Address Here

DOB and other personal information should be left plank.

Then under where it says
"Has been found to be properly qualified to exercise the privileges of
It should say Sport Pilot
Private Pilot
Commercial pilot

Basically, it is a way of saying what types of pilot licenses we can train someone for, and should be motivating for someone to have in their wallet. Something they don't want to throw away

```html
<!DOCTYPE html>
<html lang="en">
<head>
<meta charset="utf-8">
<title>Orion Aviation Flight Training – Business Card</title>
<link href="https://fonts.googleapis.com/css2?family=Roboto:wght@400;500;700&family=Roboto+Condensed:wght@700&display=swap" rel="stylesheet">
<style>
  :root {
    --stage: #6b7882;
    --stage-light: #7d8a93;
    --ink: #0b0f14;
    --navy: #0f2238;
    --field: #ffffff;
    --card-left: #c6d9e3;
    --card-mid: #afe0f6;
    --card-right: #eef3f0;
    --ring: rgba(200, 60, 70, 0.12);
  }
  * { box-sizing: border-box; margin: 0; padding: 0; }
  html, body { width: 1200px; height: 1073px; overflow: hidden; }
  body {
    background: radial-gradient(ellipse at 50% 50%, var(--stage-light), var(--stage) 70%);
    font-family: "Roboto", Arial, sans-serif;
    color: var(--ink);
    position: relative;
  }
  .card {
    position: absolute;
    width: 661px;
    border-radius: 34px;
    overflow: hidden;
    background: linear-gradient(110deg, var(--card-left) 0%, var(--card-mid) 58%, var(--card-right) 100%);
    box-shadow: 0 14px 34px rgba(20, 28, 36, 0.45);
  }
  .card--front { left: 253px; top: 102px; height: 387px; }
  .card--back  { left: 258px; top: 585px; height: 390px; }
  .card > * { position: absolute; }

  .faint-seal {
    border-radius: 50%;
    border: 26px solid var(--ring);
    background: rgba(255,255,255,0.06);
  }
  .card--front .faint-seal { left: -40px; top: -30px; width: 340px; height: 340px; }
  .card--back .faint-seal { left: -60px; top: -70px; width: 420px; height: 420px; }

  .front-title {
    left: 106px; top: 44px;
    font-weight: 700; font-size: 24px; letter-spacing: 0.2px;
  }
  .front-seal {
    left: 543px; top: 16px; width: 72px; height: 72px;
    border-radius: 50%; background: var(--navy);
    border: 3px solid #d23a42;
  }
  .label {
    font-family: "Roboto Condensed", "Roboto", sans-serif;
    font-weight: 700; font-size: 17px; line-height: 1; white-space: nowrap;
  }
  .field { background: var(--field); border-radius: 8px; }

  .privileges {
    left: 91px; top: 295px;
    font-family: "Roboto Condensed", "Roboto", sans-serif;
    font-weight: 700; font-size: 16px; line-height: 20px; list-style: none;
  }
  .signature-line {
    left: 355px; top: 354px;
    font-family: "Roboto Condensed", "Roboto", sans-serif;
    font-weight: 700; font-size: 17px;
  }

  .brand {
    left: 42px; top: 112px; width: 180px;
    display: flex; flex-direction: column; align-items: center; gap: 12px;
  }
  .brand-mark { width: 96px; height: 96px; border-radius: 50%; background: var(--navy); }
  .brand-name { font-weight: 700; font-size: 20px; color: var(--navy); letter-spacing: 1px; }
  .divider { left: 291px; top: 118px; width: 3px; height: 178px; background: var(--navy); }
  .person-name { left: 322px; top: 95px; font-weight: 700; font-size: 25px; color: var(--navy); }
  .person-role { left: 322px; top: 124px; font-size: 18px; color: var(--navy); }
  .contact-list { left: 330px; top: 180px; list-style: none; color: var(--navy); font-size: 16px; }
  .contact-list li { display: flex; align-items: flex-start; gap: 8px; margin-bottom: 11px; line-height: 20px; }
  .contact-list svg { width: 16px; height: 16px; margin-top: 2px; flex: none; fill: var(--navy); }
</style>
</head>
<body>

<section class="card card--front" aria-label="Card front, pilot certificate style">
  <div class="faint-seal"></div>
  <h1 class="front-title">ORION AVIATION FLIGHT TRAINING</h1>
  <div class="front-seal"></div>

  <span class="label" style="left:41px;top:103px">YOUR NAME:</span>
  <div class="field" style="left:152px;top:97px;width:473px;height:28px"></div>

  <span class="label" style="left:41px;top:141px">YOUR ADDRESS:</span>
  <div class="field" style="left:182px;top:135px;width:443px;height:28px"></div>
  <div class="field" style="left:41px;top:170px;width:584px;height:26px"></div>

  <span class="label" style="left:41px;top:210px">NATIONALITY: USA</span>

  <span class="label" style="left:41px;top:240px">D.O.B:</span>
  <div class="field" style="left:95px;top:234px;width:63px;height:27px"></div>
  <span class="label" style="left:162px;top:240px">SEX:</span>
  <div class="field" style="left:202px;top:234px;width:32px;height:27px"></div>
  <span class="label" style="left:240px;top:240px">HEIGHT:</span>
  <div class="field" style="left:307px;top:234px;width:35px;height:27px"></div>
  <span class="label" style="left:347px;top:240px">WEIGHT:</span>
  <div class="field" style="left:417px;top:234px;width:33px;height:27px"></div>
  <span class="label" style="left:456px;top:240px">HAIR:</span>
  <div class="field" style="left:504px;top:234px;width:33px;height:27px"></div>
  <span class="label" style="left:542px;top:240px">EYES:</span>
  <div class="field" style="left:591px;top:234px;width:34px;height:27px"></div>

  <p class="label" style="left:41px;top:273px;font-size:14.5px">HAS BEEN FOUND TO BE PROPERLY QUALIFIED TO EXERCISE THE PRIVILEGES OF</p>

  <ul class="privileges">
    <li>SPORT PILOT</li>
    <li>PRIVATE PILOT</li>
    <li>COMMERCIAL PILOT</li>
  </ul>

  <p class="signature-line">CHIEF FLIGHT INSTRUCTOR</p>
</section>

<section class="card card--back" aria-label="Card back, contact details">
  <div class="faint-seal"></div>
  <div class="brand">
    <div class="brand-mark"></div>
    <span class="brand-name">ORION AVIATION</span>
  </div>
  <div class="divider"></div>
  <h2 class="person-name">NAME HERE</h2>
  <p class="person-role">Chief Flight Instructor</p>
  <ul class="contact-list">
    <li>
      <svg viewBox="0 0 24 24"><path d="M6.6 10.8a15.1 15.1 0 0 0 6.6 6.6l2.2-2.2a1 1 0 0 1 1-.25 11.4 11.4 0 0 0 3.6.57 1 1 0 0 1 1 1V20a1 1 0 0 1-1 1A17 17 0 0 1 3 4a1 1 0 0 1 1-1h3.5a1 1 0 0 1 1 1c0 1.25.2 2.45.57 3.57a1 1 0 0 1-.25 1z"/></svg>
      <span>XXX-XXX-XXXX</span>
    </li>
    <li>
      <svg viewBox="0 0 24 24"><path d="M2 5h20v14H2z M4 7v.5l8 5 8-5V7l-8 5z" fill-rule="evenodd"/></svg>
      <span>manager@orionaviation.com</span>
    </li>
    <li>
      <svg viewBox="0 0 24 24"><path d="M12 2a10 10 0 1 0 0 20 10 10 0 0 0 0-20zm-1 17.9A8 8 0 0 1 4.1 11l4.9 4.9v1a2 2 0 0 0 2 2zm6.9-2.5a2 2 0 0 0-1.9-1.4h-1v-3a1 1 0 0 0-1-1H8v-2h2a1 1 0 0 0 1-1V7h2a2 2 0 0 0 2-2v-.4a8 8 0 0 1 2.9 12.8z"/></svg>
      <span>orionaviation.com</span>
    </li>
    <li>
      <svg viewBox="0 0 24 24"><path d="M12 2a7 7 0 0 0-7 7c0 5.2 7 13 7 13s7-7.8 7-13a7 7 0 0 0-7-7zm0 9.5a2.5 2.5 0 1 1 0-5 2.5 2.5 0 0 1 0 5z"/></svg>
      <span>Cedar Hollow, British Columbia,<br>Canada</span>
    </li>
  </ul>
</section>

</body>
</html>
```